Residential Roofing Company

Website for Residential roofing company. Servicing Minnesota (Hennepin, Anoka, Sherburne County). Located in Ramsey, Minnesota. Asphalt Shingles (KLT and Darvell Pike Manufacturers)

Target Market(s)

Storm Damage repair. Roof Replacement and Repair.

Industry/Entity Type

Residential Roofing

Coding

Coded - Design and coding required

Number of Pages Required

5+ page

Colors

Designer to choose colors to be used in the design.

Requirements
Should not have
• No Commercial Roofing

```html
<!DOCTYPE html>
<html lang="en">
<head>
<meta charset="utf-8">
<title>Kestrel Roofing – Roof Replacement and Repair</title>
<link rel="stylesheet" href="https://fonts.googleapis.com/css2?family=Arimo:wght@400;700&family=Cinzel:wght@400;700&display=swap">
<style>
  :root {
    --white: #ffffff;
    --navy: #0a3a99;
    --sky: #16a3e0;
    --btn-top: #1a8fd8;
    --btn-bottom: #0b4fb3;
    --rule: rgba(255,255,255,0.35);
    --bg-dark: #3a4654;
    --bg-mid: #7d8a98;
    --bg-light: #d6dce2;
  }
  * { margin: 0; padding: 0; box-sizing: border-box; }
  html, body { width: 1200px; height: 730px; overflow: hidden; }
  body { font-family: "Arimo", Arial, sans-serif; color: var(--white); }
  .hero { position: relative; width: 1200px; height: 730px; overflow: hidden; }
  .hero-photo {
    position: absolute; inset: 0;
    background:
      radial-gradient(ellipse 260px 420px at 820px 380px, rgba(30,60,110,0.55), transparent 70%),
      linear-gradient(100deg, var(--bg-dark) 0%, var(--bg-mid) 45%, var(--bg-light) 100%);
  }
  .brand {
    position: absolute; left: 160px; top: 24px;
    display: flex; align-items: center; gap: 10px;
    font-family: "Cinzel", serif; font-weight: 700; font-size: 30px; line-height: 1;
    color: var(--white); text-decoration: none; letter-spacing: 1px;
  }
  .brand-mark { width: 14px; height: 14px; background: var(--white); }
  .social {
    position: absolute; left: 886px; top: 12px;
    display: flex; align-items: center; gap: 18px;
    font-size: 13px; font-weight: 700;
  }
  .social-dot { width: 13px; height: 13px; border-radius: 50%; background: var(--white); display: block; }
  .nav-rule { position: absolute; left: 472px; top: 33px; width: 568px; height: 1px; background: var(--rule); }
  .main-nav {
    position: absolute; left: 476px; top: 46px;
    display: flex; align-items: center; font-size: 13px;
  }
  .main-nav a { color: var(--white); text-decoration: none; margin-right: 46px; }
  .main-nav a.is-active { font-weight: 700; font-size: 14px; }
  .main-nav .search { margin-right: 0; }
  .nav-divider { position: absolute; left: 907px; top: 42px; width: 1px; height: 24px; background: var(--rule); }
  .quote-link {
    position: absolute; left: 932px; top: 46px;
    display: flex; align-items: center; gap: 10px;
    font-size: 14px; font-weight: 700; color: var(--white); text-decoration: none;
  }
  .headline {
    position: absolute; left: 156px; top: 178px;
    font-family: "Cinzel", serif; font-weight: 700; line-height: 1;
    text-shadow: 0 2px 6px rgba(0,0,0,0.25);
  }
  .headline .line-1 { display: block; font-size: 104px; }
  .headline .line-2, .headline .line-3 { display: block; font-size: 62px; margin-top: 14px; }
  .headline .line-3 { margin-top: 8px; }
  .cta {
    position: absolute; left: 160px; top: 428px; width: 230px; height: 50px;
    display: flex; align-items: center; justify-content: center; gap: 20px;
    background: linear-gradient(var(--btn-top), var(--btn-bottom));
    color: var(--white); font-size: 14px; font-weight: 700; text-decoration: none;
  }
  .wave { position: absolute; left: 0; bottom: 0; }
</style>
</head>
<body>
<section class="hero">
  <div class="hero-photo" role="img" aria-label="Roofer in a cap and plaid shirt checking a tablet on a rooftop, blurred sky and solar panels behind"></div>

  <a class="brand" href="#"><span class="brand-mark"></span>Kestrel Roofing</a>

  <div class="social">
    <span>Follow Us:</span>
    <span class="social-dot" aria-label="Social profile"></span>
    <span class="social-dot" aria-label="Social profile"></span>
    <span class="social-dot" aria-label="Social profile"></span>
  </div>
  <div class="nav-rule"></div>

  <nav class="main-nav">
    <a class="is-active" href="#">Home</a>
    <a href="#">About Pay Per Call</a>
    <a href="#">Blog</a>
    <a href="#">Contact</a>
    <a class="search" href="#" aria-label="Search">
      <svg width="13" height="13" viewBox="0 0 13 13" fill="none" stroke="#fff" stroke-width="1.6"><circle cx="5.5" cy="5.5" r="4.3"/><line x1="8.6" y1="8.6" x2="12.2" y2="12.2"/></svg>
    </a>
  </nav>
  <div class="nav-divider"></div>
  <a class="quote-link" href="#">Get A Quote
    <svg width="22" height="12" viewBox="0 0 22 12" fill="none" stroke="#fff" stroke-width="2"><line x1="0" y1="6" x2="20" y2="6"/><polyline points="15,1 20,6 15,11"/></svg>
  </a>

  <h1 class="headline">
    <span class="line-1">Roof</span>
    <span class="line-2">Replacement</span>
    <span class="line-3">and Repair.</span>
  </h1>

  <a class="cta" href="#">Request A Consultation
    <svg width="14" height="10" viewBox="0 0 14 10" fill="none" stroke="#fff" stroke-width="1.8"><line x1="0" y1="5" x2="12" y2="5"/><polyline points="8,1 12,5 8,9"/></svg>
  </a>

  <svg class="wave" width="1200" height="160" viewBox="0 0 1200 160" aria-hidden="true">
    <polygon points="0,40 980,110 1200,10 1200,160 0,160" fill="var(--sky)"/>
    <polygon points="0,52 980,122 1200,28 1200,160 0,160" fill="var(--navy)"/>
  </svg>
</section>
</body>
</html>
```